Cool modern, tech Business card design

Looking for a new business card design for our Managed IT Services company. We would like 2 sides, with the logo one one side horizontally and then the information on the back in either vertical or horizontal. We want our colors from the logo incorporated but also would like to see the color gray in there as well.

Target Market(s)

IT, Information Technology, Tech, Service

Industry/Entity Type

It Service

Contact Information for Business Card

Carl Penner
Managing Partner
(P)555-271-4830 ext xxx
(F)555-271-4831
www.brixtelcore.com

Font styles to use
Sans Serif

Colors
959595
000000
ec1f27

Requirements
Must have
• Logo on one side with some nice design or pattern
• Information on back in either vertical or horizontal format
Nice to have
• For it to look cool, tech, modern, stand out.

```html
<!DOCTYPE html>
<html lang="en">
<head>
<meta charset="utf-8">
<title>Brixtelcore Business Card</title>
<link rel="stylesheet" href="https://fonts.googleapis.com/css2?family=Source+Sans+3:wght@300;400;600&display=swap">
<style>
  :root {
    --page-bg: #e6e6e6;
    --card-bg: #ffffff;
    --brand-red: #ec1f27;
    --brand-gray: #959595;
    --soft-gray: #d9d9d9;
    --ink: #000000;
    --text-gray: #8a8a8a;
  }
  html, body {
    margin: 0;
    width: 1200px;
    height: 1022px;
    overflow: hidden;
    background: var(--page-bg);
    font-family: "Source Sans 3", sans-serif;
  }
  .card {
    position: absolute;
    left: 75px;
    top: 211px;
    width: 1050px;
    height: 600px;
    background: linear-gradient(160deg, #ffffff 0%, #f3f3f3 100%);
    box-shadow: 0 14px 40px rgba(0,0,0,0.18);
    overflow: hidden;
  }
  .name-tab {
    position: absolute;
    left: 0;
    top: 110px;
    width: 390px;
    height: 112px;
    background: var(--brand-red);
    border-radius: 0 56px 56px 0;
    color: #fff;
    box-sizing: border-box;
    padding: 16px 0 0 46px;
  }
  .name-tab .person {
    font-size: 40px;
    font-weight: 300;
    letter-spacing: 2px;
    line-height: 1.1;
    text-transform: uppercase;
  }
  .name-tab .role {
    font-size: 23px;
    font-weight: 400;
    line-height: 1.3;
  }
  .deco-shape {
    position: absolute;
    left: 470px;
    top: -60px;
    width: 300px;
    height: 300px;
    border-radius: 50%;
    background: var(--soft-gray);
    opacity: 0.7;
  }
  .brand {
    position: absolute;
    right: 70px;
    top: 350px;
    display: flex;
    align-items: center;
    gap: 14px;
  }
  .brand .mark {
    width: 22px;
    height: 22px;
    background: var(--brand-red);
  }
  .brand .wordmark {
    font-size: 56px;
    font-weight: 600;
    color: var(--ink);
    letter-spacing: -0.5px;
  }
  .contact {
    position: absolute;
    left: 150px;
    top: 400px;
    list-style: none;
    margin: 0;
    padding: 0;
  }
  .contact li {
    display: flex;
    align-items: center;
    gap: 18px;
    height: 38px;
    font-size: 27px;
    font-weight: 300;
    color: var(--text-gray);
    letter-spacing: 0.5px;
  }
  .contact svg {
    width: 20px;
    height: 20px;
    flex: none;
  }
  .contact .web { color: #6f6f6f; }
</style>
</head>
<body>
  <div class="card">
    <div class="deco-shape" aria-hidden="true"></div>

    <div class="name-tab">
      <div class="person">Carl Penner</div>
      <div class="role">Managing Director</div>
    </div>

    <ul class="contact">
      <li>
        <svg viewBox="0 0 20 20" fill="none" stroke="#ec1f27" stroke-width="1.6"><path d="M5 2l3 4-2 2c1 2 3 4 5 5l2-2 4 3-2 3C9 17 3 11 2 5z"/></svg>
        555-271-4830
      </li>
      <li>
        <svg viewBox="0 0 20 20" fill="none" stroke="#ec1f27" stroke-width="1.6"><rect x="3" y="8" width="14" height="9"/><rect x="6" y="3" width="8" height="5"/><line x1="6" y1="12" x2="14" y2="12"/></svg>
        555-271-4831
      </li>
      <li>
        <svg viewBox="0 0 20 20" fill="none" stroke="#ec1f27" stroke-width="1.6"><rect x="2" y="4" width="16" height="12"/><path d="M2 4l8 7 8-7"/></svg>
        info@brixtelcore.com
      </li>
      <li class="web">
        <svg viewBox="0 0 20 20" fill="none" stroke="#ec1f27" stroke-width="1.6"><circle cx="10" cy="10" r="8"/><ellipse cx="10" cy="10" rx="3.5" ry="8"/><line x1="2" y1="10" x2="18" y2="10"/></svg>
        www.brixtelcore.com
      </li>
    </ul>

    <div class="brand">
      <span class="mark" aria-hidden="true"></span>
      <span class="wordmark">brixtelcore</span>
    </div>
  </div>
</body>
</html>
```